Spice Mix Label Bottle Branding - Health and Weight Loss Mixes

The company is called ZestRow Spice Mix's. We've created 5 spice mixes using ingredients that promote health and weight loss. We already have a logo but now we need labels for our bottles. We would like to see designs that have the feel of health supplements (see attached examples)

We would like a different colour featured with each of our flavours.

Our flavours are:
-Golden Chai (Yellow)
-Mild Curry (Orange)
-Coffee Rub (brown)
-Garlic Oregano (Green)
-Taco (Blue)

Thank you!

Target Market(s)

Ages 22-35. Men and Female. Trendy, Hipster.

Industry/Entity Type

Food Production

Font styles to use
Sans Serif

Colors
f37122
0655a3
0692cd
9bcb3c
fbee3f

Requirements
Must have
• A different featured colour for each flavour.
• The ZestRow Spices Logo (attached)
• The slogan: "Weight Loss Ingredients"
• -Golden Chai (Yellow)
• -Mild Curry (Orange)
• -Coffee Rub (brown)
• -Garlic Oregano (Green)
• -Taco (Blue)
• Text Files attached.
Nice to have
• A black label with a featured colour for each of the spice mice flavours.
• 'No Salt added'

```html
<!DOCTYPE html>
<html lang="en">
<head>
<meta charset="utf-8">
<title>ZestRow Spices – Bottle Labels</title>
<link rel="stylesheet" href="https://fonts.googleapis.com/css2?family=Quicksand:wght@500;600&family=Oswald:wght@600&family=Arimo:ital,wght@0,400;0,700;1,700&display=swap">
<style>
  :root {
    --page: #ffffff;
    --label-black: #000000;
    --rule: #d9d9d9;
    --ink: #ffffff;
    --taco: #1a9bd7;
    --coffee: #8a5a35;
    --garlic: #8fbc3b;
    --curry: #ea5a25;
    --chai: #d9a02a;
  }
  * { box-sizing: border-box; margin: 0; padding: 0; }
  html, body { width: 1200px; height: 960px; overflow: hidden; background: var(--page); }
  .sheet { position: relative; width: 1200px; height: 960px; }

  .label {
    position: absolute;
    width: 344px; height: 342px;
    color: var(--ink);
    font-family: "Arimo", Arial, sans-serif;
  }
  .label--taco    { --accent: var(--taco);   left: 26px;  top: 106px; }
  .label--coffee  { --accent: var(--coffee); left: 430px; top: 106px; }
  .label--garlic  { --accent: var(--garlic); left: 832px; top: 106px; }
  .label--curry   { --accent: var(--curry);  left: 234px; top: 512px; }
  .label--chai    { --accent: var(--chai);   left: 636px; top: 512px; }

  .label__shape { position: absolute; inset: 0; width: 344px; height: 342px; }
  .label__edge { fill: var(--accent); }
  .label__body { fill: var(--label-black); }
  .label__inner-line { fill: none; stroke: var(--ink); stroke-width: 1.4; }

  .brand {
    position: absolute; left: 0; right: 0; top: 60px;
    text-align: center;
  }
  .brand__name {
    display: inline-flex; align-items: center; gap: 6px;
    font-family: "Oswald", sans-serif; font-weight: 600;
    font-size: 27px; line-height: 1; letter-spacing: 0.5px;
    color: var(--ink);
  }
  .brand__mark { width: 9px; height: 9px; background: var(--accent); }
  .brand__tagline {
    display: block; margin-top: 8px;
    font-family: "Oswald", sans-serif; font-weight: 600;
    font-size: 7px; letter-spacing: 0.8px; color: var(--ink);
  }

  .rule-h {
    position: absolute; left: 40px; right: 37px; top: 161px;
    height: 1px; background: var(--rule);
  }
  .rule-v {
    position: absolute; left: 169px; top: 161px;
    width: 1px; height: 108px; background: var(--rule);
  }

  .flavour {
    position: absolute; left: 14px; width: 145px; top: 161px; height: 108px;
    display: flex; align-items: center; justify-content: flex-end;
    text-align: right;
    font-family: "Quicksand", sans-serif; font-weight: 600;
    font-size: 41px; line-height: 0.95; letter-spacing: -0.5px;
    color: var(--accent);
  }
  .flavour--single { font-size: 48px; }
  .flavour--long { font-size: 35px; }

  .ingredients {
    position: absolute; left: 178px; width: 126px; top: 173px;
    font-size: 9.3px; line-height: 1.17;
  }
  .ingredients strong { font-style: italic; font-weight: 700; }

  .no-salt {
    position: absolute; left: 45px; top: 296px;
    display: flex; align-items: center; gap: 8px;
    font-size: 10px; line-height: 1;
  }
  .no-salt svg { width: 12px; height: 12px; }
  .no-salt circle, .no-salt line { fill: none; stroke: var(--ink); stroke-width: 1.5; }

  .net-weight {
    position: absolute; left: 216px; width: 90px; top: 288px;
    text-align: center; font-weight: 700; font-size: 13px; line-height: 1.15;
  }
</style>
</head>
<body>
<main class="sheet">

  <section class="label label--taco">
    <svg class="label__shape" viewBox="0 0 344 342" aria-hidden="true">
      <polygon class="label__edge" points="24,0 320,0 344,24 344,318 320,342 24,342 0,318 0,24"/>
      <polygon class="label__body" points="27,9 317,9 335,27 335,315 317,333 27,333 9,315 9,27"/>
      <polygon class="label__inner-line" points="30,17 314,17 327,30 327,312 314,325 30,325 17,312 17,30"/>
    </svg>
    <div class="brand"><span class="brand__name"><span class="brand__mark"></span>ZestRow Spices</span><span class="brand__tagline">WEIGHT LOSS SEASONINGS</span></div>
    <div class="rule-h"></div><div class="rule-v"></div>
    <h2 class="flavour flavour--single">taco</h2>
    <p class="ingredients"><strong>INGREDIENTS:</strong> Lorem ipsum dolor sit amet, consectetuer adipiscing elit, sed diam nonummy nibh euismod</p>
    <div class="no-salt"><svg viewBox="0 0 12 12" aria-hidden="true"><circle cx="6" cy="6" r="5"/><line x1="2.5" y1="2.5" x2="9.5" y2="9.5"/></svg>NO SALT</div>
    <p class="net-weight">Net Wt.<br>10,5 oz</p>
  </section>

  <section class="label label--coffee">
    <svg class="label__shape" viewBox="0 0 344 342" aria-hidden="true">
      <polygon class="label__edge" points="24,0 320,0 344,24 344,318 320,342 24,342 0,318 0,24"/>
      <polygon class="label__body" points="27,9 317,9 335,27 335,315 317,333 27,333 9,315 9,27"/>
      <polygon class="label__inner-line" points="30,17 314,17 327,30 327,312 314,325 30,325 17,312 17,30"/>
    </svg>
    <div class="brand"><span class="brand__name"><span class="brand__mark"></span>ZestRow Spices</span><span class="brand__tagline">WEIGHT LOSS SEASONINGS</span></div>
    <div class="rule-h"></div><div class="rule-v"></div>
    <h2 class="flavour">coffee<br>rub</h2>
    <p class="ingredients"><strong>INGREDIENTS:</strong> Lorem ipsum dolor sit amet, consectetuer adipiscing elit, sed diam nonummy nibh euismod tincidunt ut laoreet dolore magna aliquam erat volutpat. Ut wisi enim ad minim veniam, quis nostrud exerci</p>
    <div class="no-salt"><svg viewBox="0 0 12 12" aria-hidden="true"><circle cx="6" cy="6" r="5"/><line x1="2.5" y1="2.5" x2="9.5" y2="9.5"/></svg>NO SALT</div>
    <p class="net-weight">Net Wt.<br>10,5 oz</p>
  </section>

  <section class="label label--garlic">
    <svg class="label__shape" viewBox="0 0 344 342" aria-hidden="true">
      <polygon class="label__edge" points="24,0 320,0 344,24 344,318 320,342 24,342 0,318 0,24"/>
      <polygon class="label__body" points="27,9 317,9 335,27 335,315 317,333 27,333 9,315 9,27"/>
      <polygon class="label__inner-line" points="30,17 314,17 327,30 327,312 314,325 30,325 17,312 17,30"/>
    </svg>
    <div class="brand"><span class="brand__name"><span class="brand__mark"></span>ZestRow Spices</span><span class="brand__tagline">WEIGHT LOSS SEASONINGS</span></div>
    <div class="rule-h"></div><div class="rule-v"></div>
    <h2 class="flavour flavour--long">garlic<br>oregano</h2>
    <p class="ingredients"><strong>INGREDIENTS:</strong> Lorem ipsum dolor sit amet, consectetuer adipiscing elit, sed diam nonummy nibh euismod tincidunt ut laoreet dolore magna aliquam erat volutpat. Ut wisi enim ad minim veniam, quis nostrud exerci</p>
    <div class="no-salt"><svg viewBox="0 0 12 12" aria-hidden="true"><circle cx="6" cy="6" r="5"/><line x1="2.5" y1="2.5" x2="9.5" y2="9.5"/></svg>NO SALT</div>
    <p class="net-weight">Net Wt.<br>10,5 oz</p>
  </section>

  <section class="label label--curry">
    <svg class="label__shape" viewBox="0 0 344 342" aria-hidden="true">
      <polygon class="label__edge" points="24,0 320,0 344,24 344,318 320,342 24,342 0,318 0,24"/>
      <polygon class="label__body" points="27,9 317,9 335,27 335,315 317,333 27,333 9,315 9,27"/>
      <polygon class="label__inner-line" points="30,17 314,17 327,30 327,312 314,325 30,325 17,312 17,30"/>
    </svg>
    <div class="brand"><span class="brand__name"><span class="brand__mark"></span>ZestRow Spices</span><span class="brand__tagline">WEIGHT LOSS SEASONINGS</span></div>
    <div class="rule-h"></div><div class="rule-v"></div>
    <h2 class="flavour">mild<br>curry</h2>
    <p class="ingredients"><strong>INGREDIENTS:</strong> Lorem ipsum dolor sit amet, consectetuer adipiscing elit, sed diam nonummy nibh euismod tincidunt ut laoreet dolore magna aliquam erat volutpat. Ut wisi enim ad minim veniam, quis nostrud exerci</p>
    <div class="no-salt"><svg viewBox="0 0 12 12" aria-hidden="true"><circle cx="6" cy="6" r="5"/><line x1="2.5" y1="2.5" x2="9.5" y2="9.5"/></svg>NO SALT</div>
    <p class="net-weight">Net Wt.<br>10,5 oz</p>
  </section>

  <section class="label label--chai">
    <svg class="label__shape" viewBox="0 0 344 342" aria-hidden="true">
      <polygon class="label__edge" points="24,0 320,0 344,24 344,318 320,342 24,342 0,318 0,24"/>
      <polygon class="label__body" points="27,9 317,9 335,27 335,315 317,333 27,333 9,315 9,27"/>
      <polygon class="label__inner-line" points="30,17 314,17 327,30 327,312 314,325 30,325 17,312 17,30"/>
    </svg>
    <div class="brand"><span class="brand__name"><span class="brand__mark"></span>ZestRow Spices</span><span class="brand__tagline">WEIGHT LOSS SEASONINGS</span></div>
    <div class="rule-h"></div><div class="rule-v"></div>
    <h2 class="flavour">golden<br>chai</h2>
    <p class="ingredients"><strong>INGREDIENTS:</strong> Lorem ipsum dolor sit amet, consectetuer adipiscing elit, sed diam nonummy nibh euismod tincidunt ut laoreet dolore magna aliquam erat volutpat. Ut wisi enim ad minim veniam, quis nostrud exerci</p>
    <div class="no-salt"><svg viewBox="0 0 12 12" aria-hidden="true"><circle cx="6" cy="6" r="5"/><line x1="2.5" y1="2.5" x2="9.5" y2="9.5"/></svg>NO SALT</div>
    <p class="net-weight">Net Wt.<br>10,5 oz</p>
  </section>

</main>
</body>
</html>
```